Website design improvement for existing site

We would like design ideas for how the inner pages (not the homepage) of www.talbrookpictures.com could be improved. We don't want to totally redesign the website. We want to improve / enhance / develop it further to look high-end, sophisticated and visually stunning.

Target Market(s)

High end video production clients. National and international TV networks and brands wanting commercial filming.

Industry/Entity Type

Videography

Other font styles liked:
• Existing site fonts

Requirements
Must have
• Improvement on the existing inner pages without totally re-working the design. We want to achieve a high-end sophisticated look with the existing branding (colours, images etc)
Nice to have
• Any ideas for improving the homepage are also welcome but we are mostly happy with this page so it is not the priority.
Should not have
• Any major changes to colours, styles etc.

```html
<!DOCTYPE html>
<html lang="en">
<head>
<meta charset="utf-8">
<title>Talbrook Pictures – About</title>
<link rel="stylesheet" href="https://fonts.googleapis.com/css2?family=Roboto:ital,wght@0,400;0,500;0,700;1,700&display=swap">
<style>
  :root {
    --red: #dc1f1f;
    --black: #000000;
    --white: #ffffff;
    --panel: #e6e6e6;
    --ink: #111111;
    --nav-grey: #b9b9b9;
    --footer-mark: #3a0707;
  }
  * { box-sizing: border-box; margin: 0; padding: 0; }
  html, body { width: 1200px; height: 2225px; overflow: hidden; }
  body { position: relative; background: var(--white); font-family: "Roboto", Arial, sans-serif; color: var(--ink); }

  .site-header { position: absolute; left: 0; top: 0; width: 1200px; height: 54px; background: var(--black); }
  .brand { position: absolute; left: 10px; top: 12px; display: flex; align-items: center; gap: 8px; }
  .brand-dot { width: 30px; height: 30px; border-radius: 50%; background: var(--red); }
  .brand-name { color: var(--white); font-weight: 500; font-size: 18px; letter-spacing: 1px; }
  .main-nav { position: absolute; right: 18px; top: 18px; display: flex; gap: 38px; }
  .main-nav a { color: var(--nav-grey); text-decoration: none; font-size: 14px; letter-spacing: 4px; }
  .main-nav a.current { color: var(--red); }

  .hero { position: absolute; left: 0; top: 54px; width: 1200px; height: 420px;
    background: radial-gradient(ellipse at 35% 55%, #6d8a9e 0%, #3c3d3f 30%, #2a2624 60%, #5a4d45 100%); }
  .hero-title { position: absolute; left: 658px; top: 304px; color: var(--white); font-weight: 700; font-size: 33px; line-height: 40px;
    text-shadow: 0 0 3px #000, 1px 1px 2px #000; }

  .section-band { position: absolute; left: 0; top: 474px; width: 1200px; height: 107px; background: var(--red);
    color: var(--white); font-weight: 500; font-size: 44px; text-align: center; line-height: 107px; }

  .profile-panel { position: absolute; background: var(--panel); }
  .profile-panel.right { left: 268px; top: 623px; width: 932px; height: 354px; border-radius: 120px 0 0 120px; }
  .profile-panel.left { left: 0; top: 983px; width: 986px; height: 354px; border-radius: 0 120px 120px 0; }

  .portrait-ring { position: absolute; width: 310px; height: 310px; border-radius: 50%; border: 40px solid var(--red); background: var(--white); }
  .portrait-ring .portrait { position: absolute; inset: 12px; border-radius: 50%; }
  .ring-one { left: 92px; top: 627px; }
  .ring-two { left: 791px; top: 1024px; }
  .portrait-one { background: linear-gradient(160deg, #4e4a45, #1d1c1c 70%); }
  .portrait-two { background: linear-gradient(160deg, #8a8a8c, #2a2727 70%); }

  .profile-text { position: absolute; font-size: 16.5px; line-height: 20.5px; }
  .profile-text h2 { font-style: italic; font-weight: 700; font-size: 22px; margin-bottom: 18px; }
  .profile-text p + p { margin-top: 20px; }
  .profile-one { left: 448px; top: 664px; width: 690px; }
  .profile-two { left: 115px; top: 1086px; width: 615px; }

  .team-band { position: absolute; left: 0; top: 1369px; width: 1200px; height: 258px; background: var(--red); }
  .team-photo { position: absolute; left: 106px; top: 31px; width: 248px; height: 196px; border: 3px solid var(--white);
    background: linear-gradient(180deg, #5a2a1e, #7a3a25 55%, #2f80c4 56%, #2a6ea8); }
  .team-text { position: absolute; left: 405px; top: 52px; width: 700px; color: var(--white); font-weight: 500; font-size: 22px; line-height: 27.5px; }

  .client-strip { position: absolute; left: 0; top: 1627px; width: 1200px; height: 143px; display: flex; align-items: center; justify-content: space-around; padding: 0 100px; }
  .client-badge { background: #d9d9d9; }
  .badge-wide { width: 104px; height: 26px; border-radius: 4px; }
  .badge-round { width: 86px; height: 86px; border-radius: 50%; }

  .site-footer { position: absolute; left: 0; top: 1770px; width: 1200px; height: 455px; background: var(--black); color: var(--white); }
  .footer-mark { position: absolute; left: 92px; top: 40px; width: 218px; height: 218px; border-radius: 50%; background: var(--footer-mark); }
  .footer-brand { position: absolute; left: 374px; top: 64px; font-weight: 500; font-size: 26px; letter-spacing: 1px; }
  .footer-details { position: absolute; left: 374px; top: 128px; font-weight: 700; font-size: 15px; line-height: 19.5px; }
  .follow { position: absolute; left: 898px; top: 58px; }
  .follow h3 { font-weight: 500; font-size: 22px; margin-bottom: 22px; }
  .social { display: flex; gap: 14px; }
  .social span { width: 53px; height: 53px; border-radius: 50%; border: 2px solid var(--red); }
  .copyright { position: absolute; left: 0; top: 241px; width: 1200px; text-align: center; font-size: 17.5px; }
</style>
</head>
<body>
  <header class="site-header">
    <div class="brand"><span class="brand-dot"></span><span class="brand-name">TALBROOK PICTURES</span></div>
    <nav class="main-nav">
      <a href="#">HOME</a>
      <a href="#" class="current">ABOUT</a>
      <a href="#">PROCESS</a>
      <a href="#">BRAND STORIES</a>
      <a href="#">CONTACT</a>
    </nav>
  </header>

  <section class="hero" role="img" aria-label="Camera monitor showing a dish with dry-ice vapour in a busy restaurant kitchen">
    <h1 class="hero-title">EXPERT CINEMATOGRAPHY.<br>BEAUTIFUL STORYTELLING.</h1>
  </section>

  <h2 class="section-band">WHO ARE WE?</h2>

  <div class="profile-panel right"></div>
  <div class="portrait-ring ring-one"><div class="portrait portrait-one" role="img" aria-label="Founder smiling while holding a cinema camera"></div></div>
  <article class="profile-text profile-one">
    <h2>Rowan Talbrook</h2>
    <p>Talbrook Pictures was set up by Rowan Talbrook. The idea? To help businesses harness the narrative power of film to tell better brand stories. To allow companies to use a creative, visual medium to produce unique and beautiful narratives. Brand messages that truly engage with customers and better define who they are.</p>
    <p>Living in Hull and working around the UK, Rowan’s a commercial filmmaker, camera operator, and director of photography. He’s worked with all the major UK terrestrial’s - Kestrelvision, Harbourline TV, Fernway &amp; Quillcast. His experience includes making brand stories, advertisements, corporate films, training videos and documentary films. He is also an ASA-approved Aerial Cinematographer and holder of a Permission for Commercial Operations for drone filming &amp; photography.</p>
  </article>

  <div class="profile-panel left"></div>
  <article class="profile-text profile-two">
    <h2>Elsie Marr</h2>
    <p>Elsie is our production assistant and b-cam operator also based in Hull. Having completed her BA (Hons) Media Production degree at the University of Ashford in 2016, Elsie has 5 years experience in photography and film.</p>
    <p>Her drive and dedication to making every shot the best it can be, and her enthusiasm for the art brings our productions to a whole new level.</p>
  </article>
  <div class="portrait-ring ring-two"><div class="portrait portrait-two" role="img" aria-label="Production assistant operating a camera in a kitchen"></div></div>

  <section class="team-band">
    <div class="team-photo" role="img" aria-label="Founder in a blue t-shirt in front of a brick wall"></div>
    <p class="team-text">Rowan collaborates with a team of skilled pre-production, production &amp; post-production specialists from Leeds and York to London. He’s worked with some of the UK’s biggest creative agencies and helped tell the brand stories of companies of all sizes and sectors, working with both agencies and businesses.</p>
  </section>

  <section class="client-strip" aria-label="Clients">
    <span class="client-badge badge-wide"></span>
    <span class="client-badge badge-round"></span>
    <span class="client-badge badge-wide"></span>
    <span class="client-badge badge-wide"></span>
    <span class="client-badge badge-wide"></span>
  </section>

  <footer class="site-footer">
    <div class="footer-mark"></div>
    <div class="footer-brand">TALBROOK PICTURES</div>
    <div class="footer-details">
      Talbrook Pictures Ltd<br>
      01632 960418 | hello@talbrookpictures.com<br>
      Company No. 10457312<br>
      VAT No. 318590417
    </div>
    <div class="follow">
      <h3>Follow us</h3>
      <div class="social"><span></span><span></span></div>
    </div>
    <p class="copyright">Copyright© 2017, @Talbrook Pictures Ltd, All Rights Reserved.</p>
  </footer>
</body>
</html>
```